THE Harrowfield Mobility Fund (HMF) PHOTOGRAPHY COMPETITION

We need a "flyer" (must be web friendly" as well as A5 Print) designed that will announce the launch of a new photography competition. The Theme of the Competition will be "Keep Moving Forward".

Harrowfield Mobility Fund will "host" a competition that is open to all comers, irrespective of experience, but within the following Classes : 1. People Living with Spinal Injuries 2. Schools 3. Amateur Under 18 Photographers 4. Amateur Over 18 Photographers 5. Charities 6. Professional Photographers.

The competition will start in October 2018 and entries will be accepted via the HMF website until 31st August 2019. Prizes to include a Cash Prize of £7,500 for the photograph that in the opinion of the judges best meets the brief. Each Class winner and runner up will receive photographic equipment (a camera for the winner, a tripod for the runner up). The two best photographs in each class will be included in HMF's 2020 Calendar. Prizes will be presented at an event in Salisbury in October 2019.

Entry Fee (payable via the HMF website) will be £2.00 per photograph.

Please note that this is an initial "draft" and any published "flyer / web page will have to meet current UK Charity Regulations.

Telephone +44 (0)1632 960418

www.hmf-example.org.uk (new website to be launched prior to Competition starting)

find us on facebook & twitter

Registered charity No. 1098472

Target Market(s)

Photographers, Schools, Charities

Industry/Entity Type

Charity

Font styles to use
Sans Serif

Colors

Designer to choose colors to be used in the design.

Requirements
Must have
• The HMF Logo
Nice to have
• Less words, high graphic appeal
Should not have
• Any doom and gloom! - People Living with Spinal Injuries are not "sick" - they are "Living With" Spinal Injury - not dieing from it!

```html
<!DOCTYPE html>
<html lang="en">
<head>
<meta charset="utf-8">
<title>Photography Competition – Keep Moving Forward</title>
<link rel="stylesheet" href="https://fonts.googleapis.com/css2?family=Libre+Baskerville:wght@700&family=Parisienne&family=Open+Sans:wght@400;600;700&display=swap">
<style>
  :root {
    --paper: #f8f8f7;
    --taupe: #7b6f60;
    --taupe-dark: #6a5f52;
    --aqua: #5cc6e3;
    --aqua-deep: #47b8d8;
    --ink-soft: #8a7f72;
    --white: #ffffff;
  }
  * { margin: 0; padding: 0; box-sizing: border-box; }
  html, body { width: 948px; height: 1200px; overflow: hidden; }
  body {
    position: relative;
    background: linear-gradient(180deg, #ffffff 0%, var(--paper) 60%, #f1f1f0 100%);
    font-family: "Open Sans", Arial, sans-serif;
    color: var(--taupe);
  }
  .flyer-title {
    position: absolute; top: 22px; left: 0; width: 948px;
    text-align: center;
    font-family: "Libre Baskerville", Georgia, serif;
    font-weight: 700; font-size: 45px; letter-spacing: 0.5px;
    color: var(--taupe);
  }
  .theme {
    position: absolute; top: 78px; left: 0; width: 948px;
    display: flex; align-items: center; justify-content: center; gap: 22px;
  }
  .theme-rule { width: 120px; height: 2px; background: var(--aqua); }
  .theme-text {
    font-family: "Parisienne", cursive;
    font-size: 58px; line-height: 70px; color: var(--aqua);
  }
  .collage { position: absolute; top: 150px; left: 0; width: 948px; height: 530px; }
  .org-name {
    position: absolute; top: 708px; left: 40px;
    display: flex; align-items: center; gap: 12px;
  }
  .org-mark { width: 30px; height: 30px; border-radius: 50%; background: var(--aqua); }
  .org-words {
    font-size: 19px; line-height: 23px; font-weight: 400;
    color: var(--taupe); letter-spacing: 1px; text-transform: uppercase;
  }
  .intro {
    position: absolute; top: 703px; left: 292px; width: 626px;
    font-size: 17px; line-height: 24px; text-align: justify; color: var(--ink-soft);
  }
  .prizes-band {
    position: absolute; top: 839px; left: 0; width: 256px; height: 42px;
    background: var(--aqua);
    clip-path: polygon(0 0, 100% 0, 96% 100%, 0 100%);
    color: var(--white); font-weight: 700; font-size: 27px;
    line-height: 42px; padding-left: 48px;
  }
  .prize-list { position: absolute; top: 903px; left: 36px; width: 420px; list-style: none; }
  .prize-item {
    position: relative; padding-left: 37px;
    font-size: 19.5px; line-height: 25px; color: var(--ink-soft);
    margin-bottom: 19px;
  }
  .prize-item:nth-child(3) { margin-bottom: 13px; }
  .prize-item strong { color: var(--taupe-dark); font-weight: 700; }
  .prize-item svg { position: absolute; left: 0; top: 0; width: 28px; height: 34px; }
  .classes-intro {
    position: absolute; top: 834px; left: 493px; width: 425px;
    font-size: 17px; line-height: 24px; text-align: justify; color: var(--ink-soft);
  }
  .class-list { position: absolute; top: 920px; left: 493px; list-style: none; }
  .class-item {
    display: flex; align-items: center; gap: 8px;
    font-size: 17.5px; line-height: 26px; color: var(--ink-soft);
  }
  .class-item svg { width: 14px; height: 14px; flex: none; }
  .contact-bar {
    position: absolute; top: 1109px; left: 170px; width: 597px; height: 42px;
    background: var(--aqua); border-radius: 12px;
    box-shadow: 0 3px 6px rgba(0,0,0,0.15);
    display: flex; align-items: center; justify-content: center; gap: 32px;
    color: var(--white); font-size: 20px; letter-spacing: 0.5px;
  }
  .contact-item { display: flex; align-items: center; gap: 12px; }
  .contact-item svg { width: 22px; height: 22px; }
  .social { position: absolute; top: 1109px; left: 819px; display: flex; gap: 13px; }
  .social-dot { width: 40px; height: 40px; border-radius: 50%; background: var(--taupe); }
  .legal {
    position: absolute; top: 1172px; left: 0; width: 948px; text-align: center;
    font-size: 10px; color: var(--taupe);
  }
</style>
</head>
<body>
  <h1 class="flyer-title">PHOTOGRAPHY COMPETITION</h1>
  <div class="theme">
    <span class="theme-rule"></span>
    <span class="theme-text">Keep Moving Forward</span>
    <span class="theme-rule"></span>
  </div>

  <svg class="collage" viewBox="0 0 948 530" role="img" aria-label="Collage of tilted photo prints showing a smiling family together in a sunny garden with a wooden chair and green foliage">
    <defs>
      <linearGradient id="garden" x1="0" y1="0" x2="1" y2="1">
        <stop offset="0" stop-color="#c9b86a"/><stop offset="1" stop-color="#6b5a3a"/>
      </linearGradient>
      <linearGradient id="chair" x1="0" y1="0" x2="0" y2="1">
        <stop offset="0" stop-color="#a8794e"/><stop offset="1" stop-color="#7a5536"/>
      </linearGradient>
      <linearGradient id="family" x1="0" y1="0" x2="1" y2="1">
        <stop offset="0" stop-color="#8a8a5e"/><stop offset="0.5" stop-color="#4f5a72"/><stop offset="1" stop-color="#3b3d4a"/>
      </linearGradient>
      <linearGradient id="mother" x1="0" y1="0" x2="0" y2="1">
        <stop offset="0" stop-color="#a89a6a"/><stop offset="0.5" stop-color="#5a4a3e"/><stop offset="1" stop-color="#3a3330"/>
      </linearGradient>
      <linearGradient id="leaves" x1="0" y1="0" x2="1" y2="1">
        <stop offset="0" stop-color="#5f8a34"/><stop offset="1" stop-color="#2f5a22"/>
      </linearGradient>
      <linearGradient id="paving" x1="0" y1="0" x2="0" y2="1">
        <stop offset="0" stop-color="#4a4038"/><stop offset="1" stop-color="#b8a48a"/>
      </linearGradient>
    </defs>
    <g stroke="#ffffff" stroke-width="4" stroke-linejoin="miter">
      <polygon points="0,45 250,15 262,250 0,290" fill="url(#garden)"/>
      <polygon points="455,108 750,102 798,510 478,515" fill="url(#paving)"/>
      <polygon points="690,100 948,85 948,420 690,430" fill="url(#leaves)"/>
      <polygon points="95,210 325,180 355,480 145,505" fill="url(#chair)"/>
      <polygon points="257,18 515,25 498,372 240,355" fill="url(#family)"/>
      <polygon points="510,12 750,0 760,280 548,305" fill="url(#mother)"/>
      <polygon points="740,77 948,98 900,420 700,390" fill="url(#leaves)"/>
    </g>
  </svg>

  <div class="org-name">
    <span class="org-mark"></span>
    <span class="org-words">Harrowfield<br>Mobility<br>Fund</span>
  </div>

  <p class="intro">The competition will start in October 2018 and entries will be accepted via the HMF website until 31st August 2019. Prizes will be presented at an event in Salisbury in October 2019. Entry Fee (payable via the HMF website) will be £2.00 per photograph.</p>

  <div class="prizes-band">PRIZES</div>
  <ul class="prize-list">
    <li class="prize-item"><svg viewBox="0 0 28 34"><path d="M8 18 L4 33 L10 29 L13 34 L14 20Z M20 18 L24 33 L18 29 L15 34 L14 20Z" fill="#5cc6e3"/><circle cx="14" cy="11" r="10" fill="#5cc6e3"/></svg><strong>£7,500</strong> Cash Prize</li>
    <li class="prize-item"><svg viewBox="0 0 28 34"><path d="M8 18 L4 33 L10 29 L13 34 L14 20Z M20 18 L24 33 L18 29 L15 34 L14 20Z" fill="#5cc6e3"/><circle cx="14" cy="11" r="10" fill="#5cc6e3"/></svg><strong>Camera</strong> for Each Class winner</li>
    <li class="prize-item"><svg viewBox="0 0 28 34"><path d="M8 18 L4 33 L10 29 L13 34 L14 20Z M20 18 L24 33 L18 29 L15 34 L14 20Z" fill="#5cc6e3"/><circle cx="14" cy="11" r="10" fill="#5cc6e3"/></svg><strong>Tripod</strong> for runner up</li>
    <li class="prize-item"><svg viewBox="0 0 28 34"><path d="M8 18 L4 33 L10 29 L13 34 L14 20Z M20 18 L24 33 L18 29 L15 34 L14 20Z" fill="#5cc6e3"/><circle cx="14" cy="11" r="10" fill="#5cc6e3"/></svg><strong>HMF's 2020 Calendar</strong> for the two best photographs in each class.</li>
  </ul>

  <p class="classes-intro">Competition that is open to all comers, irrespective of experience, but within the following Classes:</p>
  <ul class="class-list">
    <li class="class-item"><svg viewBox="0 0 14 14"><circle cx="7" cy="7" r="6" fill="none" stroke="#8a7f72" stroke-width="1.3"/><path d="M4 7.2 L6.2 9.2 L10 5" fill="none" stroke="#8a7f72" stroke-width="1.3"/></svg>People Living with Spinal Injuries</li>
    <li class="class-item"><svg viewBox="0 0 14 14"><circle cx="7" cy="7" r="6" fill="none" stroke="#8a7f72" stroke-width="1.3"/><path d="M4 7.2 L6.2 9.2 L10 5" fill="none" stroke="#8a7f72" stroke-width="1.3"/></svg>Schools</li>
    <li class="class-item"><svg viewBox="0 0 14 14"><circle cx="7" cy="7" r="6" fill="none" stroke="#8a7f72" stroke-width="1.3"/><path d="M4 7.2 L6.2 9.2 L10 5" fill="none" stroke="#8a7f72" stroke-width="1.3"/></svg>Amateur Under 18 Photographers</li>
    <li class="class-item"><svg viewBox="0 0 14 14"><circle cx="7" cy="7" r="6" fill="none" stroke="#8a7f72" stroke-width="1.3"/><path d="M4 7.2 L6.2 9.2 L10 5" fill="none" stroke="#8a7f72" stroke-width="1.3"/></svg>Amateur Over 18 Photographers</li>
    <li class="class-item"><svg viewBox="0 0 14 14"><circle cx="7" cy="7" r="6" fill="none" stroke="#8a7f72" stroke-width="1.3"/><path d="M4 7.2 L6.2 9.2 L10 5" fill="none" stroke="#8a7f72" stroke-width="1.3"/></svg>Charities</li>
    <li class="class-item"><svg viewBox="0 0 14 14"><circle cx="7" cy="7" r="6" fill="none" stroke="#8a7f72" stroke-width="1.3"/><path d="M4 7.2 L6.2 9.2 L10 5" fill="none" stroke="#8a7f72" stroke-width="1.3"/></svg>Professional Photographers</li>
  </ul>

  <div class="contact-bar">
    <span class="contact-item"><svg viewBox="0 0 22 22"><circle cx="11" cy="11" r="10" fill="#ffffff"/><path d="M8 6 L10 6 L10.6 8.6 L9.4 9.6 Q10.6 12 12.6 12.8 L13.6 11.6 L16 12.2 L16 14.2 Q15.4 15.4 13.8 15.2 Q8.4 14 6.8 8.2 Q6.8 6.6 8 6Z" fill="#5cc6e3"/></svg>+44 (0)1632 960418</span>
    <span class="contact-item"><svg viewBox="0 0 22 22"><circle cx="11" cy="11" r="10" fill="#ffffff"/><g fill="none" stroke="#5cc6e3" stroke-width="1.2"><circle cx="11" cy="11" r="6.5"/><ellipse cx="11" cy="11" rx="3" ry="6.5"/><path d="M4.5 11 H17.5 M5.5 7.8 H16.5 M5.5 14.2 H16.5"/></g></svg>www.hmf-example.org.uk</span>
  </div>
  <div class="social" aria-label="Find us on social media">
    <span class="social-dot"></span>
    <span class="social-dot"></span>
  </div>

  <p class="legal">Registered charity No. 1098472 Please note that this is an initial "draft" and any published "flyer / web page will have to meet current UK Charity Regulations.</p>
</body>
</html>
```